Lantern Path Collective

Re-design our website www.lanternpathco.org
We are a non profit catering for adults, elderly, veterans and youth in impoverished neighborhoods to improve their digital access and help them improve their lives and better our community.

I need the text on home page to stay. Its the first message vsitors shd read when they arrive on our page.

Number of Pages Required

4 page

Font styles to use
Other font styles liked:
• color and font shd be like the image attched below.

```html
<!DOCTYPE html>
<html lang="en">
<head>
<meta charset="utf-8">
<title>Lantern Path Collective – Home</title>
<link href="https://fonts.googleapis.com/css2?family=Varela+Round&family=Montserrat:wght@400;500;600&display=swap" rel="stylesheet">
<style>
:root{
  --stage:#a9a8a9;
  --white:#ffffff;
  --mist:#eeeff2;
  --brand:#2f80e8;
  --brand-deep:#1f56a3;
  --ink:#1b1b1b;
  --footer:#474747;
  --footer-base:#3d3d3d;
  --footer-text:#e6e6e6;
}
*{box-sizing:border-box;margin:0;padding:0}
html,body{width:847px;height:1200px;overflow:hidden;background:var(--stage)}
body{position:relative;font-family:"Montserrat",Arial,sans-serif;color:var(--ink)}
.page{position:absolute;left:160px;top:107px;width:672px;height:1300px;transform:scale(.784);transform-origin:0 0;background:var(--white);overflow:hidden}
.abs{position:absolute}

/* header */
.site-header{position:absolute;left:0;top:0;width:672px;height:40px;background:var(--white);z-index:3}
.brand-tile{position:absolute;left:76px;top:0;width:64px;height:67px;background:var(--brand);color:var(--white);font-family:"Varela Round",sans-serif;font-size:10px;line-height:1.2;display:flex;align-items:center;justify-content:center;text-align:center;padding:6px;z-index:4}
.main-nav{position:absolute;left:182px;top:15px;display:flex;gap:14px;font-size:7px;font-weight:500}
.main-nav span{white-space:nowrap}
.main-nav .active{color:var(--brand)}
.main-nav .drop::after{content:"";display:inline-block;width:3px;height:3px;border-right:1px solid var(--ink);border-bottom:1px solid var(--ink);transform:rotate(45deg);margin:0 0 2px 4px}
.donate{position:absolute;left:531px;top:11px;width:56px;height:20px;border-radius:3px;background:var(--brand);color:var(--white);font-size:8px;font-weight:600;display:flex;align-items:center;justify-content:center;letter-spacing:.3px}

/* hero */
.hero{position:absolute;left:0;top:40px;width:672px;height:260px;background:var(--mist)}
.hero-title{position:absolute;left:76px;top:102px;font-family:"Varela Round",sans-serif;font-size:22px;line-height:27px;color:var(--brand);font-weight:400}
.hero-sub{position:absolute;left:76px;top:176px;font-size:11px;line-height:14px;font-weight:500}
.story{position:absolute;left:0;top:240px;width:672px;height:540px}
.story-copy{position:absolute;left:290px;top:360px;width:310px;color:var(--white);font-size:7.5px;line-height:12.1px;text-align:justify}
.story-copy p{margin-bottom:12px}

/* services */
.services-title{position:absolute;left:0;width:672px;top:821px;text-align:center;font-family:"Varela Round",sans-serif;font-weight:400;font-size:18px;line-height:22.5px;color:var(--brand)}
.services-intro{position:absolute;left:144px;width:384px;top:877px;text-align:center;font-size:8.6px;line-height:11px;font-weight:500}
.service-card{position:absolute;top:972px;width:123px;height:81px;background:var(--brand-deep);border-radius:3px;color:var(--white);font-size:8.5px;line-height:11px;text-align:center;display:flex;align-items:center;justify-content:center;padding:14px 10px 0}
.service-icon{position:absolute;left:42px;top:-20px;width:39px;height:39px;border-radius:50%;background:var(--brand);border:2px solid var(--white);display:flex;align-items:center;justify-content:center}

/* footer */
.site-footer{position:absolute;left:0;top:1100px;width:672px;height:140px;background:var(--footer);color:var(--footer-text)}
.footer-brand{position:absolute;left:76px;top:40px;width:64px;font-family:"Varela Round",sans-serif;font-size:10px;line-height:12px;color:var(--white)}
.footer-col{position:absolute;top:41px;font-size:6.6px;line-height:8.8px}
.footer-col h3{font-family:"Montserrat",sans-serif;font-weight:500;font-size:8.6px;line-height:11px;letter-spacing:.3px;color:var(--white);margin-bottom:8px;text-transform:uppercase}
.social{display:flex;gap:3px;margin-top:8px}
.social i{display:block;width:10px;height:10px;border-radius:2px;background:var(--white)}
.footer-base{position:absolute;left:0;top:1240px;width:672px;height:60px;background:var(--footer-base);color:var(--footer-text);text-align:center;font-size:6.6px}
.footer-base .policy{position:absolute;left:0;width:672px;top:17px;letter-spacing:.3px}
.footer-base .copyright{position:absolute;left:0;width:672px;top:35px}
</style>
</head>
<body>
<div class="page">

  <header class="site-header">
    <div class="brand-tile">Lantern Path Collective</div>
    <nav class="main-nav">
      <span class="active">Home</span>
      <span class="drop">Get Connected</span>
      <span class="drop">e-Waste Service</span>
      <span>Our Impact</span>
      <span class="drop">About</span>
      <span>Contact</span>
    </nav>
    <div class="donate">DONATE</div>
  </header>

  <section class="hero">
    <h1 class="hero-title">Creating a Social<br>Impact with e-Waste</h1>
    <p class="hero-sub">by transforming Unwanted Technology<br>into Opportunities for People In-Need.</p>
  </section>

  <section class="story">
    <svg class="abs" style="left:0;top:0" width="672" height="540" viewBox="0 0 672 540">
      <defs>
        <linearGradient id="storyBg" x1="0" y1="0" x2="1" y2="1">
          <stop offset="0" stop-color="#2d74d6"/>
          <stop offset=".5" stop-color="#3a86e6"/>
          <stop offset="1" stop-color="#2f74d4"/>
        </linearGradient>
      </defs>
      <path d="M0 8 C160 10 260 30 360 40 C480 50 600 30 672 16 L672 540 L0 540 Z" fill="url(#storyBg)"/>
    </svg>
  </section>

  <svg class="abs" style="left:330px;top:62px" width="260" height="252" viewBox="0 0 260 252" role="img" aria-label="Photo of three children smiling together at a laptop">
    <defs>
      <clipPath id="heroCircle"><circle cx="128" cy="125" r="125"/></clipPath>
      <linearGradient id="kidsPhoto" x1="0" y1="0" x2="1" y2="0">
        <stop offset="0" stop-color="#3c7d54"/>
        <stop offset=".5" stop-color="#c9a08a"/>
        <stop offset="1" stop-color="#eea456"/>
      </linearGradient>
    </defs>
    <circle cx="128" cy="125" r="125" fill="var(--brand)"/>
    <rect x="0" y="70" width="260" height="190" fill="url(#kidsPhoto)" clip-path="url(#heroCircle)" opacity=".9"/>
  </svg>

  <svg class="abs" style="left:70px;top:402px" width="200" height="252" viewBox="0 0 200 252">
    <defs>
      <linearGradient id="seniorsPhoto" x1="0" y1="0" x2="1" y2="1">
        <stop offset="0" stop-color="#f1ece6"/><stop offset="1" stop-color="#9fa6b4"/>
      </linearGradient>
      <linearGradient id="groupPhoto" x1="0" y1="0" x2="1" y2="1">
        <stop offset="0" stop-color="#8c6d52"/><stop offset=".6" stop-color="#d9c8b0"/><stop offset="1" stop-color="#5f7fb8"/>
      </linearGradient>
    </defs>
    <g role="img" aria-label="Photo of an older couple taking a picture with a tablet">
      <circle cx="71" cy="70" r="69" fill="var(--white)"/>
      <circle cx="71" cy="70" r="66" fill="url(#seniorsPhoto)"/>
    </g>
    <g role="img" aria-label="Photo of a group of adults working together around a laptop">
      <circle cx="126" cy="180" r="69" fill="var(--white)"/>
      <circle cx="126" cy="180" r="66" fill="url(#groupPhoto)"/>
    </g>
  </svg>

  <div class="story-copy">
    <p>Lantern Path Collective is a nonprofit and social enterprise that creates equitable access to opportunity by providing devices, internet access, digital skills training, and tech support for low-income families, the homeless, and Veterans in our communities while at the same time, empowering businesses and organizations to do good by diverting technology from landfills to protect our planet.</p>
    <p>Being digitally literate is no longer a luxury, it is a must-have skill for everyone to manage information, communicate, manage money, and access support plus other government services. It has become an essential tool for modern-day citizenship and participation; no one can afford to be left behind.</p>
    <p>Unfortunately, nearly 100 million Americans lack access to a personal computer, internet connection, or both. This lack of access to digital technology creates a significant gap between the opportunities unconnected people can access and the ones digitally native households can. This gap in opportunities is known as the digital divide, and it's our mission by joining hands with many other organizations that are tirelessly trying to shrink it because we believe that equitable access to information and technology empowers people to achieve their fullest potential.</p>
    <p>At the same time Electronic waste, or e-waste, refers to electronic products and components that are unwanted, unusable, or nearing the end of their useful life. While e-waste only makes up 2% of the mass in landfills, it accounts for 70% of toxic waste. Unfortunately, recycling is no longer a sufficient method for disposing of waste sustainably; given the scale of the climate crisis, reuse is now a prerequisite for protecting our planet.</p>
  </div>

  <h2 class="services-title">Explore Opportunities Online with Low-Cost<br>Technology, Internet, Training &amp; Support</h2>
  <p class="services-intro">In order to comprehensively shrink the digital divide, we offer you access to low-cost computers, low-cost internet, free digital literacy training and tech support. Click the boxes below to explore how we can help you and members of your community unlock their full potential through digital technology.</p>

  <div class="service-card" style="left:76px">
    <div class="service-icon"><svg width="18" height="16" viewBox="0 0 18 16" fill="none" stroke="#fff" stroke-width="1.3"><rect x="3" y="2" width="12" height="8" rx="1"/><path d="M1 13h16"/></svg></div>
    Affordable<br>Technology
  </div>
  <div class="service-card" style="left:209px">
    <div class="service-icon"><svg width="18" height="16" viewBox="0 0 18 16" fill="none" stroke="#fff" stroke-width="1.5" stroke-linecap="round"><path d="M1 6a11 11 0 0 1 16 0"/><path d="M4 9a7 7 0 0 1 10 0"/><path d="M7 12a3 3 0 0 1 4 0"/><circle cx="9" cy="14.3" r=".8" fill="#fff"/></svg></div>
    Internet Access
  </div>
  <div class="service-card" style="left:342px">
    <div class="service-icon"><svg width="18" height="18" viewBox="0 0 18 18" fill="none" stroke="#fff" stroke-width="1.3" stroke-linecap="round"><circle cx="9" cy="8" r="4"/><path d="M7.5 13h3M7.8 15h2.4M9 1v1.5M2.5 8H1M17 8h-1.5M3.8 3l1 1M14.2 3l-1 1"/></svg></div>
    Digital Literacy<br>Training
  </div>
  <div class="service-card" style="left:474px">
    <div class="service-icon"><svg width="18" height="18" viewBox="0 0 18 18" fill="none" stroke="#fff" stroke-width="1.4" stroke-linecap="round"><path d="M3 10V8a6 6 0 0 1 12 0v2"/><rect x="2" y="9" width="3" height="5" rx="1"/><rect x="13" y="9" width="3" height="5" rx="1"/><path d="M15 14c0 2-2 3-5 3"/></svg></div>
    Tech Support
  </div>

  <footer class="site-footer">
    <div class="footer-brand">Lantern Path Collective</div>
    <div class="footer-col" style="left:179px">
      <h3>Get Connected</h3>
      Get Technology<br>Low-Cost Internet<br>Digital Training<br>Tech Support<br>For Organizations
    </div>
    <div class="footer-col" style="left:286px">
      <h3>Purpose with<br>Tech</h3>
      E-Waste Services<br>Data Destruction<br>Technology Drives
    </div>
    <div class="footer-col" style="left:389px">
      <h3>About Us</h3>
      About<br>Our Impact
    </div>
    <div class="footer-col" style="left:483px;top:39px">
      <h3>Contact</h3>
      (555) 014-0192<br>hello@lanternpathco.org<br>&nbsp;418 Harbor Lane, Fairview,<br>CA 90000
      <div class="social"><i></i><i></i><i></i><i></i></div>
    </div>
  </footer>
  <div class="footer-base">
    <div class="policy">PRIVACY &amp; SECURITY POLICY</div>
    <div class="copyright">© 2023 by Lantern Path Collective. All rights reserved.</div>
  </div>

</div>
</body>
</html>
```